Quorvella Website Redesign

We need a redesign of the company website.

We're a company, based in the UK, called Quorvella. We develop software for the Healthcare Industry, used by medical professionals throughout the UK on a daily basis.

We have a suite of tools that form the Quorvella Platform, and all are web-based.

We want to communicate that our software is not only innovative but is the best available, easy to use, and provides exceptional quality and RoI.

Additionally, we want our existing customers to be able to see what else we can offer them.

A site map is attached.
Updates

Hi Everyone,

As we approach the deadline for submissions, we’ve shortlisted threedesigns that we felt were the best of the submissions and have asked thedesigners to make some additional changes and produce some content pages so wecan see what’s beneath the Home page in the rest of the site.

Thank you all for your submissions – there was an awful lot ofdisagreement among everyone here over which designs we thought were best andsome of those that haven’t made it into the final three were very well liked.

Those in the final three have been messaged individually and have theirdesigns as the only non-eliminated ones showing. We would ask at this stagethat anyone not in the final three please do no further work or submitadditional designs as we are approaching the deadline and will not be able toprovide sufficient feedback to allow any changes in a short space of time.

Kind regards,
The Quorvella Team

Target Market(s)

Nurses and medical professionals in western-speaking countries, most notably in the UK.

Predominantly, we expect it will be senior medical staff that will be viewing (and using) our website - some will be existing customers and some will be new or potential customers.

Industry/Entity Type

Medical

Requirements
Must have
• Area to showcase and provide information about products.
• Company information - who we are and why you should choose us.
• News and events - blog, archive newsletters, publications, etc.
• Support section for existing customers - FAQ, Forum, Manuals.
• Contact page.
• We also feel that we'd like to have our telephone number and primary email address visible at all times, with an immediate ability for users to request a demonstration.
Nice to have
• A "My Quorvella" area would be nice at some point, though that's something for further down the line.

```html
<!DOCTYPE html>
<html lang="en">
<head>
<meta charset="utf-8">
<title>Quorvella – Products and Services</title>
<link href="https://fonts.googleapis.com/css2?family=Noto+Sans:wght@400;700&display=swap" rel="stylesheet">
<style>
:root{
  --blue:#0a8fe6;
  --blue-deep:#1a8be8;
  --grey-text:#6f6f6f;
  --dark-text:#3b3b3b;
  --rule:#e2e2e2;
  --panel-border:#dcdcdc;
  --box-border:#c9dff7;
  --contact-top:#f4f9ff;
  --contact-bottom:#a9d3fb;
  --white:#ffffff;
}
*{box-sizing:border-box;margin:0;padding:0}
html,body{width:765px;height:1200px;overflow:hidden;background:var(--white)}
body{position:relative;font-family:"Noto Sans",Verdana,sans-serif;color:var(--dark-text)}

.brand{position:absolute;left:18px;top:20px;font-size:21px;font-weight:400;color:var(--blue-deep);line-height:26px}

.quick-icons{position:absolute;left:338px;top:12px;display:flex;gap:34px}
.quick-icons svg{width:28px;height:28px}

.main-nav{position:absolute;left:16px;top:72px;width:431px;height:44px;border-radius:7px;
  background:linear-gradient(#1b95ee,#3fb2fb 60%,#7dd0ff);display:flex;align-items:center;padding-left:5px}
.main-nav a{color:var(--white);font-size:9.5px;text-decoration:none;padding:0 10px;border-left:1px solid rgba(255,255,255,.85);line-height:15px}
.main-nav a:first-child{border-left:none}

.products-panel{position:absolute;left:15px;top:127px;width:432px;height:978px;border:1px solid var(--panel-border);border-radius:8px;padding:10px 11px 0 11px}
.panel-title{font-size:13px;font-weight:400;color:var(--dark-text);padding-left:4px;height:34px;line-height:20px}
.globe-art{position:absolute;left:282px;top:10px;width:122px;height:72px;border-radius:50%/40%;
  background:radial-gradient(circle at 55% 45%,#3d8fe0 0,#2f6ab8 25%,#4a4a4a 45%,#cfcfcf 70%,transparent 72%)}

.product{border-bottom:1px solid var(--rule);width:400px;padding:20px 0 0 4px;height:97px}
.product.first{height:69px;padding-top:0}
.product.short{height:75px}
.product h3{font-size:9.5px;font-weight:700;color:var(--blue);letter-spacing:.4px;line-height:14px}
.product p{font-size:8px;color:var(--grey-text);letter-spacing:.4px;line-height:18px;width:408px}

.section-title{font-size:11px;font-weight:400;color:var(--dark-text);letter-spacing:.4px;padding-left:4px;margin-top:18px;line-height:16px}
.audit{padding:10px 0 0 4px}
.audit h3{font-size:9.5px;font-weight:700;color:var(--blue);letter-spacing:.4px;line-height:14px}
.audit p{font-size:8px;color:var(--grey-text);letter-spacing:.4px;line-height:13.5px;text-align:justify;width:408px;margin-top:2px}
.audit.spaced{padding-top:0;margin-top:28px}
.tech{padding-left:4px;margin-top:2px}
.tech p{font-size:8px;color:var(--grey-text);letter-spacing:.4px;line-height:27px}

.team-photo{position:absolute;left:458px;top:160px;width:297px;height:205px;
  background:linear-gradient(90deg,#7c8fd9 0%,#e9ecf3 40%,#f4f4f4 55%,#7f92d8 80%,#6b7fca 100%)}

.contact-heading{position:absolute;left:459px;top:424px;font-size:12.5px;font-weight:400;color:var(--blue)}
.contact-box{position:absolute;left:453px;top:444px;width:277px;height:199px;border:1px solid var(--box-border);border-radius:7px;
  background:linear-gradient(var(--contact-top),#d5eaff 45%,var(--contact-bottom));padding:10px 0 0 15px}
.contact-box p{font-size:9.5px;line-height:16px;color:var(--dark-text)}
.contact-box .gap{margin-top:9px}
.mail-art{position:absolute;left:180px;top:4px;width:54px;height:92px;background:linear-gradient(#1a73d8 0%,#3f95ea 55%,rgba(160,200,240,.3) 100%)}

.side-box{position:absolute;left:453px;width:277px;border:1px solid var(--box-border);border-radius:7px;background:var(--white)}
.news-box{top:663px;height:147px;padding:11px 0 0 10px}
.side-box h2{font-size:12.5px;font-weight:400;color:var(--blue);padding-left:4px;line-height:16px}
.news-box ul{list-style:none;margin-top:12px}
.news-box li{font-size:8.5px;color:var(--grey-text);line-height:23px;letter-spacing:.3px}
.news-box li::before{content:"> ";color:var(--dark-text);font-weight:700}
.more{font-size:8.5px;color:var(--grey-text);letter-spacing:.3px;text-align:right}
.news-box .more{padding-right:30px;line-height:12px}
.my-box{top:832px;height:124px;padding:9px 0 0 10px}
.my-box p{font-size:8.5px;color:var(--grey-text);line-height:20px;width:170px;margin-top:8px;letter-spacing:.3px}
.my-box .more{color:var(--blue);padding-right:10px;margin-top:2px;width:auto}
.people-art{position:absolute;left:183px;top:6px;width:60px;height:54px;border-radius:12px;background:linear-gradient(90deg,#b05a2a,#5a4a3a 50%,#3d3d3d)}

.footer-nav{position:absolute;left:37px;top:1130px;width:710px;height:33px;border-radius:5px;
  background:linear-gradient(#1b95ee,#3fb2fb 60%,#7dd0ff);display:flex;align-items:center;justify-content:center}
.footer-nav a{color:var(--white);font-size:7.5px;text-decoration:none;letter-spacing:.3px}
.legal{position:absolute;top:1173px;left:245px;font-size:7.5px;color:var(--grey-text);letter-spacing:.4px}
.legal span+span{margin-left:84px}
</style>
</head>
<body>

<header class="brand">Quorvella Health</header>

<div class="quick-icons">
  <svg viewBox="0 0 28 28" aria-label="Home">
    <path d="M3 14 L14 4 L25 14 Z" fill="#d8452d"/>
    <rect x="6" y="13" width="16" height="12" fill="#e8d2a6"/>
    <rect x="9" y="16" width="4" height="9" fill="#6b3b1f"/>
    <rect x="16" y="16" width="4" height="4" fill="#5aa7e6"/>
  </svg>
  <svg viewBox="0 0 28 28" aria-label="Write to us">
    <path d="M3 11 L14 4 L25 11 L25 25 L3 25 Z" fill="#f2f2f2" stroke="#9a9a9a"/>
    <path d="M3 11 L14 18 L25 11" fill="none" stroke="#9a9a9a"/>
    <path d="M10 18 L22 4 L25 7 L13 21 L9 22 Z" fill="#f4b63c" stroke="#8a6a2a" stroke-width=".6"/>
  </svg>
</div>

<nav class="main-nav">
  <a href="#">Products &amp; Services</a>
  <a href="#">About Quorvella</a>
  <a href="#">News &amp; Events</a>
  <a href="#">Support</a>
  <a href="#">My Quorvella</a>
</nav>

<main class="products-panel">
  <h1 class="panel-title">Products and Services</h1>
  <div class="globe-art" role="img" aria-label="Stethoscope wrapped around a globe"></div>

  <section class="product first">
    <h3>Clinical Systems</h3>
    <p style="margin-top:8px">Cleft Patient Management System</p>
    <p style="margin-top:6px">An end-to-end electronic patient records solution for Cleft departments.</p>
  </section>
  <section class="product">
    <h3>Tissue Viability Management System</h3>
    <p style="margin-top:8px">Cleft Patient Management System</p>
    <p style="margin-top:6px">An end-to-end electronic patient records solution for Cleft departments.</p>
  </section>
  <section class="product">
    <h3>SENTRY – Infection Control Management System</h3>
    <p style="margin-top:8px;line-height:17px">Electronic Pressure Ulcer Record System that tracks and reports on patients Pressure Ulcers, grading, progress or degradation.</p>
  </section>
  <section class="product">
    <h3>Electronic Patient Record</h3>
    <p style="margin-top:3px">An integrated view of the patient's electronic records through an intuitive, easy to use, web based portal.</p>
  </section>
  <section class="product">
    <h3>Radiology Information System</h3>
    <p style="margin-top:7px;text-align:justify">Radiology Information System with full support for internal/external electronic referrals, Radiology Workflow and DICOM Modality Integration.</p>
  </section>
  <section class="product short">
    <h3>Ward and Bed Management</h3>
    <p style="margin-top:7px">Electronic ward and bed state tracking.</p>
  </section>
  <section class="product short">
    <h3>Patient Medication Tracker</h3>
    <p style="margin-top:3px">An electronic tracking tool for monitoring patients current and past medications.</p>
  </section>

  <h2 class="section-title">Clinical Audit Tools</h2>
  <section class="audit">
    <h3>Saving Lives</h3>
    <p>An electronic data capture and reporting module that greatly simplifies the implementation of the Saving Lives Programme and eliminates the need to aggregate data and generate reports.</p>
  </section>
  <section class="audit spaced">
    <h3>Standards Toolkit</h3>
    <p>An electronic audit tool focused on quality and standards of care.</p>
  </section>
  <section class="audit spaced">
    <h3>Clinical Indicators</h3>
    <p>An electronic tracking tool for monitoring patients current and past medications.</p>
  </section>

  <h2 class="section-title" style="margin-top:26px">Technology Services</h2>
  <div class="tech">
    <p>Software Development Services</p>
    <p>Integration Services</p>
  </div>
</main>

<div class="team-photo" role="img" aria-label="Three smiling healthcare professionals in scrubs and a lab coat"></div>

<h2 class="contact-heading">Contact Information</h2>
<aside class="contact-box">
  <div class="mail-art" role="img" aria-label="Blue envelope illustration"></div>
  <p>Quorvella</p>
  <p>48 Harlow Crescent</p>
  <p>London N7 2QB</p>
  <p>United Kingdom</p>
  <p>Tel.: +44 (0) 208 555 0142</p>
  <p>Fax: +44 (0) 208 555 0198</p>
  <p class="gap">Republic Of Ireland</p>
  <p>Tel.: +353 (0) 861 555 017</p>
  <p class="gap">Greece and Cyprus</p>
  <p>Tel.: +357 995 55021</p>
</aside>

<aside class="side-box news-box">
  <h2>Latest News</h2>
  <ul>
    <li>Lorem ipsum dolor sit amet, consectetuer adipiscing</li>
    <li>elit. Mauris placerat, arcu vel pharetra iaculis,</li>
    <li>purus viverra nisl, ac semper diam metus ut ante.</li>
    <li>congue, turpis at scelerisque facilisis, elit enim</li>
  </ul>
  <p class="more">Read More&gt;&gt;</p>
</aside>

<aside class="side-box my-box">
  <h2>My Quorvella</h2>
  <div class="people-art" role="img" aria-label="Two user avatar figures"></div>
  <p>Lorem ipsum dolor sit amet, consectetuer adipiscing elit. Mauris placerat, arcu vel pharetra iaculis,</p>
  <p class="more">Read More&gt;&gt;</p>
</aside>

<nav class="footer-nav">
  <a href="#" style="margin-right:34px">Home</a>
  <a href="#" style="margin-right:28px">Contact</a>
  <a href="#" style="margin-right:17px">Products &amp; Services</a>
  <a href="#" style="margin-right:22px">About Quorvella</a>
  <a href="#" style="margin-right:25px">News &amp; Events</a>
  <a href="#" style="margin-right:31px">Support</a>
  <a href="#">My Quorvella</a>
</nav>

<footer class="legal"><span>Copyright © 2008 Quorvella Ltd</span><span>Terms of Use</span></footer>

</body>
</html>
```